FotoVELD buisnesscard

Hey :) I need a modern buisnesscard for my company FotoVELD
It most have:
Dagligleder og Fotograf: Eirik Tobias Vangsnes

Mob: +4791642508
Epost: post@fotoveld-eks.no
Adresse: Bjørkeveien22, 4870 Fjordvik

Facbook and instagram logo with text FotoVELD

FotoVELD logo

It Company

```html
<!DOCTYPE html>
<html lang="no">
<head>
<meta charset="utf-8">
<title>FotoVELD business card</title>
<link href="https://fonts.googleapis.com/css2?family=Khand:wght@600&family=Roboto:wght@400;700&display=swap" rel="stylesheet">
<style>
  :root {
    --page: #e4e4e4;
    --card-grey: #9a9b9d;
    --card-grey-light: #b4b5b7;
    --card-grey-dark: #8e9092;
    --card-white: #f4f4f4;
    --ink-white: #ffffff;
    --ink-soft: #eeeeee;
    --ink-grey: #8a8b8d;
    --swoosh: #6f7072;
  }
  html, body {
    margin: 0;
    width: 1200px;
    height: 576px;
    overflow: hidden;
    background: var(--page);
    font-family: "Roboto", sans-serif;
  }
  .canvas {
    position: relative;
    width: 1200px;
    height: 576px;
  }
  .card {
    position: absolute;
    border-radius: 7px;
    overflow: hidden;
    box-shadow: 0 2px 4px rgba(0,0,0,0.18);
  }
  .brand-name {
    position: absolute;
    margin: 0;
    font-family: "Roboto", sans-serif;
    font-weight: 700;
    line-height: 1;
    text-align: center;
    letter-spacing: 0.5px;
  }
  .brand-square {
    position: absolute;
    border-radius: 3px;
  }

  .card-front {
    left: 82px;
    top: 139px;
    width: 484px;
    height: 293px;
    background: linear-gradient(180deg, var(--card-grey-light) 0%, var(--card-grey) 55%, var(--card-grey-dark) 100%);
  }
  .card-front .brand-square {
    left: 208px;
    top: 94px;
    width: 68px;
    height: 68px;
    background: var(--ink-white);
  }
  .card-front .brand-name {
    left: 0;
    width: 484px;
    top: 172px;
    font-size: 36px;
    color: var(--ink-white);
  }

  .card-back {
    left: 602px;
    top: 138px;
    width: 480px;
    height: 292px;
    background: var(--card-grey);
  }
  .back-shape {
    position: absolute;
    inset: 0;
  }
  .person-name {
    position: absolute;
    left: 24px;
    top: 28px;
    margin: 0;
    font-family: "Khand", sans-serif;
    font-weight: 600;
    font-size: 22px;
    color: var(--ink-white);
    line-height: 1;
  }
  .person-role {
    position: absolute;
    left: 24px;
    top: 55px;
    margin: 0;
    font-size: 12px;
    color: var(--ink-soft);
  }
  .contact-list {
    position: absolute;
    left: 24px;
    top: 179px;
    margin: 0;
    padding: 0;
    list-style: none;
    font-size: 13px;
    color: var(--ink-white);
  }
  .contact-list li {
    display: flex;
    align-items: center;
    height: 18px;
  }
  .contact-list svg {
    width: 11px;
    height: 11px;
    margin-right: 12px;
    fill: var(--ink-white);
  }
  .social-line {
    position: absolute;
    left: 24px;
    top: 242px;
    display: flex;
    align-items: center;
    font-size: 13px;
    color: var(--ink-white);
  }
  .social-square {
    width: 14px;
    height: 14px;
    background: var(--ink-white);
    border-radius: 2px;
    margin-right: 10px;
  }
  .card-back .brand-square {
    left: 334px;
    top: 101px;
    width: 62px;
    height: 62px;
    background: var(--ink-grey);
  }
  .card-back .brand-name {
    left: 272px;
    width: 190px;
    top: 168px;
    font-size: 30px;
    color: var(--ink-grey);
  }
</style>
</head>
<body>
<main class="canvas">
  <section class="card card-front">
    <span class="brand-square" aria-hidden="true"></span>
    <p class="brand-name">FotoVELD</p>
  </section>

  <section class="card card-back">
    <svg class="back-shape" viewBox="0 0 480 292" aria-hidden="true">
      <path d="M312 0 C252 80 242 200 298 292 L480 292 L480 0 Z" fill="var(--card-white)"/>
      <path d="M300 0 C278 30 266 80 264 130 C272 70 292 28 320 0 Z" fill="var(--swoosh)"/>
    </svg>

    <h1 class="person-name">Eirik Tobias Vangsnes</h1>
    <p class="person-role">Managing Director &amp; Photographer</p>

    <ul class="contact-list">
      <li>
        <svg viewBox="0 0 12 12"><path d="M3 0h6a1 1 0 0 1 1 1v10a1 1 0 0 1-1 1H3a1 1 0 0 1-1-1V1a1 1 0 0 1 1-1zm.5 1.5v8h5v-8zM6 10a.6.6 0 1 0 0 1.2A.6.6 0 0 0 6 10z"/></svg>
        +4791642508
      </li>
      <li>
        <svg viewBox="0 0 12 12"><path d="M0 2h12v8H0zm1 1v.3l5 3.2 5-3.2V3zm0 1.5V9h10V4.5L6 7.7z"/></svg>
        post@fotoveld-eks.no
      </li>
      <li>
        <svg viewBox="0 0 12 12"><path d="M6 0a4 4 0 0 1 4 4c0 3-4 8-4 8S2 7 2 4a4 4 0 0 1 4-4zm0 2.5a1.5 1.5 0 1 0 0 3 1.5 1.5 0 0 0 0-3z"/></svg>
        Bjørkeveien22, 4870 Fjordvik
      </li>
    </ul>

    <div class="social-line">
      <span class="social-square"></span>
      /FotoVELD
    </div>

    <span class="brand-square" aria-hidden="true"></span>
    <p class="brand-name">FotoVELD</p>
  </section>
</main>
</body>
</html>
```